Web Site Redesign

We operate a data centre facility specialing in colocation and Fibre optic connectivity (i.e. point to point fibre services and internet over fibre).

We have an existing site located at www.norvalex.example however this is very very tired and requires a redesign. We are looking for a fresh new design that will be appealing to potential customers.

The Company name is Norva eX and the primary corporate colour is bright red with secondary colours of white, grey and black. Specific bright red can be seen in attached company logo.

Website needs to be modern, clean and professional representing our premium colocation and fibre provider branding.

Our company slogan is : safe. secure. reliable

We will provide feedback regardless of the quality of the design to ensure a better outcome for all parties.

Please feel free to contact us if you have any questions.

# The designer can use placeholder images or feel free to use any/all or none of the attached images
# The designer can use sample filler text

Target Market(s)

Technical IT Professionals as well C level executives (i.e. CEO's, CIO).

Industry/Entity Type

Internet

Requirements
Must have
• clean design
Nice to have
• A sidebar with two sections. 1 for current promo and 1 for "Let us call you back/contact you"
Should not have
• Clutter

```html
<!DOCTYPE html>
<html lang="en">
<head>
<meta charset="utf-8">
<title>Norva eX – Safe, Secure &amp; Reliable Data Centre</title>
<link href="https://fonts.googleapis.com/css2?family=Alegreya:wght@400;700&family=Comfortaa:wght@500&family=Arimo:wght@400;700&display=swap" rel="stylesheet">
<style>
  :root {
    --brand-red: #d71c1c;
    --deep-red: #b51010;
    --title-red: #7a1616;
    --ink: #1a1a1a;
    --black: #000;
    --white: #fff;
    --grey-light: #eeeeee;
    --grey-mid: #cfcfcf;
    --grey-text: #333;
  }
  * { box-sizing: border-box; margin: 0; padding: 0; }
  html, body { width: 938px; height: 1200px; overflow: hidden; }
  body { position: relative; background: var(--white); font-family: "Arimo", Arial, sans-serif; color: var(--ink); }

  .site-header { position: absolute; left: 0; top: 0; width: 938px; height: 137px; background: var(--black); }
  .brand { position: absolute; left: 28px; top: 44px; display: flex; align-items: center; gap: 10px; }
  .brand-mark { width: 30px; height: 30px; background: var(--brand-red); }
  .brand-name { font-family: "Arimo", Arial, sans-serif; font-size: 30px; font-weight: 400; color: var(--white); }
  .phone { position: absolute; right: 24px; top: 22px; display: flex; align-items: center; gap: 6px; color: var(--white); font-family: "Alegreya", serif; font-style: italic; font-size: 24px; letter-spacing: 1px; }
  .main-nav { position: absolute; right: 14px; top: 83px; display: flex; gap: 4px; }
  .main-nav a { color: var(--white); text-decoration: none; font-weight: 700; font-size: 12.5px; padding: 5px 10px; border-radius: 12px; }
  .main-nav a.active { background: var(--white); color: var(--brand-red); padding: 5px 16px; margin-right: 6px; }

  .hero { position: absolute; left: 21px; top: 123px; width: 901px; height: 436px; border-radius: 6px; background: linear-gradient(#ffffff, #f3f3f3 60%, #e6e6e6); box-shadow: 0 1px 4px rgba(0,0,0,.25); overflow: hidden; }
  .hero-photo { position: absolute; right: 0; top: 0; width: 340px; height: 436px; background: linear-gradient(160deg, #f4e7df 0%, #e1443f 45%, #c81a1a 75%, #d8d8d8 100%); }
  .hero-title { position: absolute; left: 32px; top: 70px; font-family: "Alegreya", serif; font-weight: 700; font-size: 52px; color: var(--brand-red); text-shadow: 1px 2px 2px rgba(0,0,0,.25); }
  .hero-text { position: absolute; left: 24px; top: 120px; width: 560px; font-family: "Alegreya", serif; font-size: 21px; line-height: 30px; color: var(--ink); }
  .btn { display: inline-block; background: var(--brand-red); color: var(--white); font-weight: 700; font-size: 12px; text-decoration: none; padding: 6px 10px; border-radius: 5px; box-shadow: 0 1px 3px rgba(0,0,0,.4); }
  .hero .btn { position: absolute; left: 22px; top: 182px; font-size: 14px; padding: 6px 13px; border: 2px solid var(--white); }
  .slider-tab { position: absolute; left: 760px; top: 352px; width: 150px; height: 47px; background: var(--brand-red); border-radius: 8px 0 0 8px; display: flex; align-items: center; padding-left: 15px; gap: 6px; color: var(--white); font-weight: 700; font-size: 12px; }
  .slider-tab i { width: 12px; height: 12px; border-radius: 50%; background: var(--white); }
  .slider-tab i.current { background: var(--black); }
  .slider-tab span { margin-left: 16px; }

  .feature { position: absolute; top: 592px; height: 162px; border: 2px solid var(--grey-mid); border-radius: 12px; background: linear-gradient(#f4f4f4, #ffffff 35%); padding: 8px 14px; }
  .feature h2 { font-family: "Alegreya", serif; font-weight: 400; font-size: 20px; color: var(--ink); }
  .feature p { font-size: 10.5px; line-height: 13.5px; letter-spacing: .3px; margin-top: 3px; }
  .feature .lead { font-weight: 700; margin-top: 12px; }
  .feature .btn { position: absolute; bottom: -10px; }
  .partner-row { display: flex; gap: 30px; margin-top: 14px; align-items: center; }
  .partner-badge { height: 26px; background: var(--grey-light); border-radius: 4px; }

  .welcome { position: absolute; left: 21px; top: 805px; width: 613px; height: 297px; background: #fafafa; }
  .panel-head { height: 37px; background: var(--grey-light); padding: 6px 10px; font-family: "Comfortaa", sans-serif; font-size: 23px; color: var(--title-red); }
  .welcome-body { padding: 10px 12px; font-size: 11px; line-height: 17px; color: var(--grey-text); }
  .welcome-body p { margin-bottom: 8px; }
  .divider { position: absolute; left: 648px; top: 805px; height: 300px; border-left: 1px dotted #999; }
  .sidebar { position: absolute; left: 664px; top: 805px; width: 261px; height: 297px; background: #fafafa; }
  .sidebar p { padding: 10px 9px; font-size: 11px; line-height: 17px; color: var(--grey-text); }
  .rack-photo { position: absolute; left: 12px; top: 104px; width: 240px; height: 146px; border: 5px solid var(--white); box-shadow: 0 1px 4px rgba(0,0,0,.4); background: linear-gradient(90deg, #2a3440, #7d8a96 35%, #3a4550 60%, #a2adb8); }
  .sidebar .btn { position: absolute; left: 172px; top: 265px; }

  .footer-card { position: absolute; left: 16px; top: 1100px; width: 910px; height: 44px; background: var(--white); border-radius: 0 0 8px 8px; }
  .site-footer { position: absolute; left: 0; top: 1126px; width: 938px; height: 74px; background: var(--black); }
  .site-footer::before { content: ""; position: absolute; left: 16px; top: 0; width: 910px; height: 19px; background: var(--white); border-radius: 0 0 8px 8px; }
  .footer-nav { position: absolute; left: 30px; top: 41px; color: var(--white); font-weight: 700; font-size: 12px; }
  .footer-nav a { color: var(--white); text-decoration: none; }
  .copyright { position: absolute; right: 27px; top: 41px; color: var(--white); font-weight: 700; font-size: 12px; }
</style>
</head>
<body>
  <header class="site-header">
    <div class="brand"><span class="brand-mark"></span><span class="brand-name">Norva eX</span></div>
    <div class="phone">
      <svg width="38" height="30" viewBox="0 0 38 30" aria-hidden="true">
        <path d="M4 10 Q19 0 34 10 L31 15 Q27 13 26 9 Q19 6 12 9 Q11 13 7 15 Z" fill="#1f6fc9"/>
        <rect x="9" y="14" width="20" height="14" rx="3" fill="#1f6fc9"/>
        <circle cx="19" cy="21" r="4" fill="#fff"/>
      </svg>
      +61 8 9000 4821
    </div>
    <nav class="main-nav">
      <a class="active" href="#">HOME</a><a href="#">About Us</a><a href="#">Facilities</a><a href="#">Business Continuity</a><a href="#">Services</a><a href="#">Partners</a><a href="#">Webmail</a><a href="#">Contact Us</a>
    </nav>
  </header>

  <section class="hero">
    <div class="hero-photo" role="img" aria-label="Smiling woman in a red top working on a white laptop"></div>
    <h1 class="hero-title">Safe, Secure &amp; Reliable</h1>
    <p class="hero-text">Perth's Safe, Secure &amp; Reliable Data Centre"Talk to us about designing a solution to meet your needs.</p>
    <a class="btn" href="#">Read More</a>
    <div class="slider-tab"><i></i><i></i><i></i><i class="current"></i><span>Play</span></div>
  </section>

  <article class="feature" style="left:26px;width:268px">
    <h2>Business Continuity</h2>
    <p>No matter how safe and secure you feel right now, the stability of your entire organisation could be under serious threat! Whether a natural disaster such as fire or flood, or man made issue such as arson or theft, these disasters could cause untold damage to your IT infrastructure.</p>
    <a class="btn" href="#" style="left:144px">Read More</a>
  </article>
  <article class="feature" style="left:342px;width:263px">
    <h2>Norva eX Services</h2>
    <p>Norva eX currently offers colocation services with unsurpassed reliability and speed to hundreds of Australian based and international clients.</p>
    <p class="lead">Innovative IT Solutions...</p>
    <a class="btn" href="#" style="left:144px">Read More</a>
  </article>
  <article class="feature" style="left:657px;width:267px">
    <h2 style="padding-left:20px">Partners</h2>
    <p>Norva eX partners with Australia's leading providers of IT solutions and infrastructure.</p>
    <div class="partner-row">
      <span class="partner-badge" style="width:82px;margin-left:18px"></span>
      <span class="partner-badge" style="width:54px;height:34px;border-radius:50%"></span>
    </div>
    <a class="btn" href="#" style="left:148px">Read More</a>
  </article>

  <section class="welcome">
    <h2 class="panel-head">Welcome To &nbsp;Norva eX</h2>
    <div class="welcome-body">
      <p>A world class data centre in the safest place on Earth.</p>
      <p>With a centrally located data centre in the heart of the Perth CBD Norva eX is excellently positioned to assist with your critical IT requirements.</p>
      <p>The CBD facility features overlapping power grids, redundant power supplies and comprehensively maintained infrastructure, providing excellent levels of protection for your critical IT equipment. The State's newest and most technologically advanced data centre is also now open in Belmont, a convenient 5.5 km's from the CBD providing a perfect location for either production sites, or DR infrastructure.</p>
      <p>From Government departments to large corporations to SME's, Norva eX is the ideal company to assist with your colocation requirements. With warm racks already provisioned, you can begin using the data centre almost immediately.</p>
      <p>Call us today to see how we can help meet your needs.</p>
    </div>
  </section>
  <div class="divider"></div>
  <aside class="sidebar">
    <h2 class="panel-head">Norva eX Services</h2>
    <p>Norva eX currently offers colocation services with unsurpassed reliability and speed to hundreds of Australian based and international clients.</p>
    <div class="rack-photo" role="img" aria-label="Row of server racks inside the data centre"></div>
    <a class="btn" href="#">Read More</a>
  </aside>

  <footer class="site-footer">
    <div class="footer-nav"><a href="#">Home</a> | <a href="#">About Us</a> | <a href="#">Facilities</a> | <a href="#">Business Continuity</a> | <a href="#">Services</a> | <a href="#">Partners</a> | <a href="#">Webmail</a> | <a href="#">Contact Us</a></div>
    <div class="copyright">Copyright @ 2010 Norva eX &nbsp;All Rights Reserved</div>
  </footer>
</body>
</html>
```